label design for oral care product

Kindly invite you to design bottle label (114 mm*40 mm) for our product, a kind of oral care product. The GEL is different from our previous cleanser product, as the pic we uploaded for demonstration. The color of frosted glass bottle is dark green, but the cap is white. You could download the pic of bottle among the uploaded files. The logo file and label content description are attached too. Please check them. Our product is made from many kinds of natural plant extracts, which includes herb and fruit. I wish the label would make our product look high-end and reliable. And it would be better if you could give some advice on paper material and special requirements for printing, related to your design. I value the texture of label too, because I think that stands for the quality of products. No color limitation for the use of our logo.
Target Market(s)
20-40 female, who value oral health.
Colors
Designer to choose colors to be used in the design.
Look and feel
Each slider illustrates characteristics of the customer's brand and the style your logo design should communicate.

```html
<!DOCTYPE html>
<html lang="en">
<head>
<meta charset="utf-8">
<title>Aligner Gel Label</title>
<link href="https://fonts.googleapis.com/css2?family=Open+Sans:wght@400;600;700&family=Open+Sans+Condensed:wght@300;700&family=Nunito:wght@900&display=swap" rel="stylesheet">
<style>
  :root {
    --bg: #b9babd;
    --paper: #ffffff;
    --teal: #2ed6da;
    --aqua: #22bfd6;
    --blue: #1d75c8;
    --deep-blue: #1a5fb8;
    --ink: #6f6f6f;
    --ink-dark: #4a4a4a;
  }
  html, body {
    margin: 0;
    width: 1200px;
    height: 1100px;
    overflow: hidden;
    background: linear-gradient(180deg, #a9aaad 0%, #c4c5c8 100%);
    font-family: "Open Sans", Arial, sans-serif;
  }
  .label {
    position: absolute;
    left: 41px;
    top: 303px;
    width: 798px;
    height: 353px;
    background: var(--paper);
    transform: scale(1.4);
    transform-origin: top left;
    overflow: hidden;
  }
  .label-waves {
    position: absolute;
    inset: 0;
    width: 798px;
    height: 353px;
  }
  .info-panel {
    position: absolute;
    left: 16px;
    top: 22px;
    width: 194px;
  }
  .info-heading {
    height: 23px;
    line-height: 23px;
    padding-left: 6px;
    color: #fff;
    font-size: 10px;
    font-weight: 700;
    background: linear-gradient(90deg, var(--aqua) 0%, var(--teal) 35%, var(--deep-blue) 100%);
  }
  .directions-box {
    border: 1px solid var(--blue);
    border-top: none;
    height: 84px;
    box-sizing: border-box;
    padding: 6px 6px;
  }
  .info-text {
    margin: 0;
    font-size: 7.6px;
    line-height: 1.55;
    color: var(--ink);
    text-align: justify;
  }
  .contains-heading { margin-top: 11px; }
  .contains-text { padding: 10px 0 0; }
  .origin {
    margin-top: 14px;
    font-size: 7.6px;
    font-weight: 700;
    color: var(--ink);
  }
  .front-panel {
    position: absolute;
    left: 250px;
    top: 0;
    width: 290px;
    text-align: center;
  }
  .product-name {
    margin: 34px 0 0;
    font-size: 24px;
    font-weight: 600;
    letter-spacing: 0.5px;
    background: linear-gradient(90deg, var(--teal), var(--blue));
    -webkit-background-clip: text;
    background-clip: text;
    color: transparent;
  }
  .claim-band {
    margin: 6px 5px 0;
    height: 24px;
    line-height: 24px;
    background: linear-gradient(90deg, var(--aqua), var(--teal));
    color: #fff;
    font-size: 13px;
    letter-spacing: 0.2px;
  }
  .tagline-small {
    margin-top: 14px;
    font-size: 9px;
    color: var(--aqua);
  }
  .tagline-large {
    font-size: 21px;
    line-height: 1.1;
    color: var(--aqua);
  }
  .tagline-small.bottom { margin-top: 1px; }
  .brand-name {
    position: absolute;
    left: 0;
    right: 0;
    top: 222px;
    font-family: "Nunito", "Open Sans", sans-serif;
    font-weight: 900;
    font-size: 40px;
    color: var(--teal);
    letter-spacing: 0.5px;
  }
  .volume {
    position: absolute;
    left: 0;
    right: 0;
    top: 339px;
    font-size: 7px;
    color: #fff;
  }
</style>
</head>
<body>
  <div class="label">
    <svg class="label-waves" viewBox="0 0 798 353" role="img" aria-label="Flowing blue and turquoise waves with scattered bubble rings">
      <defs>
        <linearGradient id="wave-blue" x1="0" y1="1" x2="1" y2="0">
          <stop offset="0" stop-color="#2bc8dc"/>
          <stop offset="0.5" stop-color="#1e8fd0"/>
          <stop offset="1" stop-color="#1a62bd"/>
        </linearGradient>
        <linearGradient id="wave-teal" x1="0" y1="0" x2="1" y2="0">
          <stop offset="0" stop-color="#2ee0dc"/>
          <stop offset="0.6" stop-color="#2ab8df"/>
          <stop offset="1" stop-color="#1f85cf"/>
        </linearGradient>
      </defs>
      <path d="M420,330 C560,300 690,215 798,150 L798,353 L420,353 Z" fill="url(#wave-blue)"/>
      <path d="M0,318 C180,322 360,320 480,306 C560,296 620,300 798,330 L798,353 L0,353 Z" fill="url(#wave-teal)" opacity="0.9"/>
    </svg>

    <section class="info-panel">
      <div class="info-heading">DIRECTIONS:</div>
      <div class="directions-box">
        <p class="info-text">Drop on the teeth directly after brushing. Or, put into clear aligners before wearing again. No need to rinse your mouth with water.</p>
      </div>
      <div class="info-heading contains-heading">CONTAINS:</div>
      <p class="info-text contains-text">A proprietary blend of natural plant extract including Angelica, Radix Rehmanniae, Coptis, Honeysuckle, Echinacea, Sage, Chamomile, Acerola cherry.</p>
      <div class="origin">Made in Taiwan</div>
    </section>

    <section class="front-panel">
      <h1 class="product-name">ALIGNER GEL</h1>
      <div class="claim-band">IMMUNE SUPPORT FOR ORAL HEALTH</div>
      <div class="tagline-small">THE SOLUTION TO MAINTAIN</div>
      <div class="tagline-large">DENTAL HYGIENE</div>
      <div class="tagline-small bottom">AND STRENGTHEN GUMS</div>
      <div class="brand-name">Glintly</div>
      <div class="volume">30 ML / 1 FL OZ</div>
    </section>
  </div>
</body>
</html>
```